Family Medicine Clinic Needs Mailchimp Newsletter Template

Looking for a responsive mailchimp template that matches the theme and overall look/feel of our website brightpathhc.com.

I'm looking for a professional, clean, simple, minimalist, bold design.
Colors would ideally be greens and blues, cool tones, muted colors, or graytones.

See attached word document for content for the upcoming newsletter

Can see prior newsletter content here:
http://brightpathhc.com/ourresources/newsletter-archive/

I have attached a copy of our brochure to see a sample of what we offer

The desired newsletter title would be:
The Bright Path
Looking for a great banner for that

Looking for basically 1 main photo area per text area for future templates

Under September is Comfort Outreach Month want links to our different services I mention

Under the videos section would like a video gallery of sorts that have links to the videos

Lumaderm image ad needs to be redone

Would like a button to take to schedule an appointment and patient portal
Easily visible phone number
Would like to have several sections with buttons to find out more

Would like feedback question at bottom
Rated 7-10 would forward to
https://zipqa.lnk/Rb8kWe

1-6 would send email to us

Reason: I have now guaranteed payment so I am giving a few more days for those designers that still want to submit a design

```html
<!DOCTYPE html>
<html lang="en">
<head>
<meta charset="utf-8">
<title>The Bright Path — Bright Path Family Medicine Newsletter</title>
<link href="https://fonts.googleapis.com/css2?family=Roboto:wght@400;500;700;900&display=swap" rel="stylesheet">
<style>
:root{
  --blue:#2fa0d8;
  --blue-deep:#2590c7;
  --green:#8cc63f;
  --green-dark:#6fa32a;
  --ink:#2b2b2b;
  --text:#4a4a4a;
  --muted:#8a8a8a;
  --rule:#e3e3e3;
  --gray-band:#ececec;
  --footer:#2a2a2a;
  --white:#ffffff;
}
*{box-sizing:border-box;margin:0;padding:0}
html,body{width:1200px;height:3516px;overflow:hidden}
body{position:relative;background:var(--white);font-family:"Roboto",Arial,sans-serif;color:var(--text)}
.abs{position:absolute}
svg.band{position:absolute;left:0;display:block}

/* header */
.brand{left:70px;top:40px;display:flex;align-items:center;gap:16px}
.brand-dot{width:58px;height:58px;border-radius:50%;background:var(--green)}
.brand-name{font-weight:700;font-size:44px;line-height:1;color:var(--green-dark)}
.brand-name small{display:block;font-size:17px;letter-spacing:4px;margin-top:6px}
.phone{left:745px;top:16px;color:var(--white);font-weight:700;font-size:22px;display:flex;align-items:center;gap:10px}
.pill{border-radius:30px;font-weight:700;text-transform:uppercase;display:flex;align-items:center;justify-content:center;gap:10px}
.portal{left:945px;top:10px;width:180px;height:38px;background:var(--white);color:var(--ink);font-size:14px}
.schedule{left:811px;top:80px;width:314px;height:52px;background:var(--green);color:var(--white);font-size:16px;box-shadow:0 4px 0 var(--green-dark)}

/* hero */
.hero-photo{left:540px;top:145px;width:660px;height:440px;background:linear-gradient(135deg,#e9ede4 0%,#d9c4b0 45%,#a8c48a 100%)}
.hero-title{left:129px;top:312px;font-size:66px;font-weight:700;color:var(--green)}
.hero-title span{color:var(--blue)}

/* side panels */
.panel{background:var(--green);color:var(--ink);display:flex;align-items:center}
.panel h2{font-weight:900;text-transform:uppercase;line-height:1.05}
.panel h2 em{font-style:normal;font-size:28px;font-weight:700;display:block}

/* ticks */
.tick{position:relative;padding-left:34px}
.tick::before{content:"";position:absolute;left:0;top:-1px;width:20px;height:20px;border:2px solid var(--green);border-radius:50%}
.tick::after{content:"";position:absolute;left:7px;top:3px;width:5px;height:9px;border:solid var(--green);border-width:0 3px 3px 0;transform:rotate(45deg)}

.issue-list{list-style:none;font-size:15px;color:var(--text)}
.issue-list li{position:absolute;white-space:nowrap}
.follow{left:933px;top:710px;width:215px;font-size:15px;line-height:1.5}
.like-badge{left:933px;top:790px;width:42px;height:16px;background:#dbe4f1;border:1px solid #b7c3d8;border-radius:2px}

.btn{background:var(--green);color:var(--white);font-size:13px;height:50px;box-shadow:0 4px 0 var(--green-dark);letter-spacing:.5px}

.section-title{font-weight:700;font-size:30px;text-transform:uppercase;color:var(--ink);text-align:center;width:1200px;left:0}
.know-title{left:75px;top:1030px;font-size:30px;font-weight:700;color:var(--ink);text-transform:uppercase}
.know-item{width:345px;font-size:14px;line-height:1.55;top:1087px}

/* services */
.service{width:360px;text-align:center;color:var(--white);font-size:19px;font-weight:500}
.service-icon{width:94px;height:94px;border-radius:50%;background:var(--white);margin:0 auto 30px}
.svc-rule-v{width:1px;background:rgba(255,255,255,.35)}
.svc-rule-h{height:1px;background:rgba(255,255,255,.35)}

/* video */
.thumb{width:197px;height:145px;border:3px solid #d8d8d8;background:linear-gradient(160deg,#c9b8a8,#5a6a7c);display:flex;align-items:center;justify-content:center}
.play{width:44px;height:34px;background:var(--white);border-radius:8px;position:relative}
.play::after{content:"";position:absolute;left:17px;top:9px;border-style:solid;border-width:8px 0 8px 13px;border-color:transparent transparent transparent var(--ink)}

/* gallery */
.shot{border:3px solid var(--white);background:linear-gradient(150deg,#f0d2bd,#d5a589)}
.shot b{position:absolute;left:10px;bottom:8px;color:var(--white);font-size:12px;font-weight:700;font-style:italic;letter-spacing:.5px}

/* feedback */
.fb-q{left:431px;top:3012px;width:700px;font-size:21px;line-height:1.4;color:var(--blue);font-weight:500}
.scale-end{top:3102px;font-size:13px;font-weight:700;color:var(--ink)}
.scale{left:425px;top:3131px;width:675px;display:flex;justify-content:space-between;font-size:16px;font-weight:500;color:var(--ink)}
.scale .hi{color:var(--green-dark)}
.fb-note{left:431px;top:3180px;width:680px;font-size:14px;line-height:1.6}

/* footer */
.foot-brand{left:0;width:1200px;top:3318px;display:flex;justify-content:center;align-items:center;gap:14px}
.foot-brand .brand-dot{width:46px;height:46px}
.foot-brand .brand-name{font-size:36px;color:var(--white)}
.copyright{left:0;width:1200px;top:3418px;text-align:center;font-size:12px;color:var(--muted)}
.social{left:0;width:1200px;top:3456px;display:flex;justify-content:center;gap:22px}
.social span{width:26px;height:26px;background:#8a8a8a;border-radius:3px}
</style>
</head>
<body>

<!-- header band -->
<svg class="band" style="top:0" width="1200" height="150" viewBox="0 0 1200 150" aria-hidden="true">
  <path d="M0 0H1200V55C900 70 600 0 300 20C180 28 80 38 0 30Z" fill="var(--blue)"/>
</svg>
<div class="abs brand">
  <span class="brand-dot"></span>
  <span class="brand-name">Bright Path<small>FAMILY MEDICINE</small></span>
</div>
<div class="abs phone">
  <svg width="18" height="18" viewBox="0 0 24 24" aria-hidden="true"><path fill="#fff" d="M6.6 10.8a15 15 0 0 0 6.6 6.6l2.2-2.2a1 1 0 0 1 1-.25 11.4 11.4 0 0 0 3.6.57 1 1 0 0 1 1 1V20a1 1 0 0 1-1 1A17 17 0 0 1 3 4a1 1 0 0 1 1-1h3.5a1 1 0 0 1 1 1c0 1.25.2 2.45.57 3.57a1 1 0 0 1-.25 1Z"/></svg>
  (555) 240-7318
</div>
<div class="abs pill portal">
  <svg width="14" height="14" viewBox="0 0 24 24" aria-hidden="true"><path fill="var(--ink)" d="M12 12a5 5 0 1 0 0-10 5 5 0 0 0 0 10Zm0 2c-4 0-9 2-9 6v2h18v-2c0-4-5-6-9-6Z"/></svg>
  Patient Portal
</div>
<div class="abs pill schedule">
  <svg width="18" height="18" viewBox="0 0 24 24" aria-hidden="true"><path fill="#fff" d="M7 2v2H4v18h16V4h-3V2h-2v2H9V2Zm-1 8h12v10H6Z"/></svg>
  Schedule an Appointment
</div>

<!-- hero -->
<div class="abs hero-photo" role="img" aria-label="Photo of a smiling family of four outdoors, children riding on their parents' backs"></div>
<h1 class="abs hero-title">The Bright <span>Path</span></h1>
<svg class="band" style="top:540px" width="1200" height="80" viewBox="0 0 1200 80" aria-hidden="true">
  <path d="M0 40C300 0 800 10 1200 40V80H0Z" fill="var(--white)"/>
</svg>

<!-- in this issue -->
<svg class="band" style="top:551px" width="370" height="430" viewBox="0 0 370 430" aria-hidden="true">
  <path d="M0 0L342 35V185L364 205L342 225V429L0 429Z" fill="var(--green)"/>
</svg>
<div class="abs panel" style="left:75px;top:730px">
  <h2 style="font-size:36px"><em>In</em>This Issue</h2>
</div>
<ul class="issue-list">
  <li class="tick" style="left:405px;top:672px">Comfort Outreach Month</li>
  <li class="tick" style="left:405px;top:714px">15 minutes of fame</li>
  <li class="tick" style="left:405px;top:756px">It's Official</li>
  <li class="tick" style="left:405px;top:799px">Don't Operate, Regenerate!</li>
  <li class="tick" style="left:405px;top:841px">Back to School Lumaderm Special</li>
  <li class="tick" style="left:691px;top:672px">Your Sinus Solution</li>
  <li class="tick" style="left:691px;top:714px">Breast Thermography</li>
  <li class="tick" style="left:691px;top:756px">Get Fit for Fall</li>
  <li class="tick" style="left:691px;top:799px">Recipe of the Month</li>
  <li class="tick" style="left:691px;top:841px">Feedback Wanted</li>
</ul>
<p class="abs follow">Please like and follow us on Circlepage! We share regular updates and health tips.</p>
<div class="abs like-badge"></div>

<!-- what you need to know -->
<svg class="band" style="top:930px" width="1200" height="70" viewBox="0 0 1200 70" aria-hidden="true">
  <path d="M0 50L342 50V0H0Z M342 50C600 20 800 10 858 10V0H342Z" fill="var(--white)"/>
</svg>
<svg class="band" style="top:937px" width="1200" height="360" viewBox="0 0 1200 360" aria-hidden="true">
  <path d="M858 0H1200V340L858 360V200L836 180L858 160Z" fill="var(--green)"/>
</svg>
<h2 class="abs know-title">What You Need to Know</h2>
<p class="abs tick know-item" style="left:75px">Nearly 100 million Americans experience chronic pain more than those who have diabetes, heart disease and cancer combined.</p>
<p class="abs tick know-item" style="left:452px">Nearly 100 million Americans experience chronic pain more than those who have diabetes, heart disease and cancer combined.</p>
<div class="abs pill btn" style="left:75px;top:1198px;width:183px">Find Out More ›</div>
<div class="abs" style="left:900px;top:1060px;width:226px;text-align:right;color:var(--white);font-weight:900;text-transform:uppercase">
  <div style="font-size:29px">September is</div>
  <div style="font-size:35px;color:var(--ink);line-height:1.1">Comfort Outreach</div>
  <div style="font-size:29px">Month!</div>
</div>

<!-- services -->
<svg class="band" style="top:1270px" width="1200" height="700" viewBox="0 0 1200 700" aria-hidden="true">
  <path d="M0 55C400 -10 800 -10 1200 55V620C800 700 400 690 0 610Z" fill="var(--blue)"/>
</svg>
<h2 class="abs section-title" style="top:1356px;color:var(--white)">Our Services</h2>
<div class="abs svc-rule-v" style="left:420px;top:1440px;height:330px"></div>
<div class="abs svc-rule-v" style="left:780px;top:1440px;height:330px"></div>
<div class="abs svc-rule-h" style="left:70px;top:1608px;width:1060px"></div>
<div class="abs service" style="left:61px;top:1439px"><div class="service-icon" role="img" aria-label="Icon of a patient receiving manipulation on a table"></div>Osteopathic Manipulation</div>
<div class="abs service" style="left:420px;top:1439px"><div class="service-icon" role="img" aria-label="Icon of a patient receiving acupuncture"></div><span style="position:relative;top:12px">Acupuncture</span></div>
<div class="abs service" style="left:781px;top:1439px"><div class="service-icon" role="img" aria-label="Icon of a syringe"></div>Prolo/PRP/Stem Cell Injections</div>
<div class="abs service" style="left:61px;top:1640px"><div class="service-icon" role="img" aria-label="Icon of a spine"></div>Spinal Decompression</div>
<div class="abs service" style="left:420px;top:1640px"><div class="service-icon" role="img" aria-label="Icon of a sauna room"></div>Infrared Sauna</div>
<div class="abs service" style="left:781px;top:1640px"><div class="service-icon" role="img" aria-label="Icon of an oxygen molecule"></div>Hyperbaric Oxygen</div>
<div class="abs pill btn" style="left:509px;top:1845px;width:183px">Find Out More ›</div>

<!-- video gallery -->
<h2 class="abs section-title" style="top:2008px">Video Gallery</h2>
<div class="abs thumb" style="left:73px;top:2079px" role="img" aria-label="Video still of a woman with glasses speaking"><span class="play"></span></div>
<div class="abs thumb" style="left:288px;top:2079px" role="img" aria-label="Video still of a woman speaking indoors"><span class="play"></span></div>
<div class="abs thumb" style="left:504px;top:2079px" role="img" aria-label="Video still of a woman in a clinic"><span class="play"></span></div>
<div class="abs thumb" style="left:715px;top:2079px" role="img" aria-label="Video still of a woman in an exam room"><span class="play"></span></div>
<div class="abs thumb" style="left:930px;top:2079px" role="img" aria-label="Video still of a woman in a dark blazer speaking"><span class="play"></span></div>
<div class="abs pill btn" style="left:509px;top:2265px;width:183px">Find Out More ›</div>

<!-- lumaderm gallery -->
<svg class="band" style="top:2340px" width="1200" height="600" viewBox="0 0 1200 600" aria-hidden="true">
  <path d="M0 15L1200 15V565C800 600 400 600 0 560Z" fill="var(--gray-band)"/>
</svg>
<h2 class="abs section-title" style="top:2432px">Lumaderm Gallery</h2>
<div class="abs shot" style="left:77px;top:2498px;width:199px;height:141px" role="img" aria-label="Before: forehead with frown lines"><b>BEFORE</b></div>
<div class="abs shot" style="left:295px;top:2498px;width:199px;height:141px" role="img" aria-label="After: smooth forehead"><b>AFTER</b></div>
<div class="abs shot" style="left:77px;top:2662px;width:199px;height:141px" role="img" aria-label="Before: smile with lines around the eyes"><b>BEFORE</b></div>
<div class="abs shot" style="left:295px;top:2662px;width:199px;height:141px" role="img" aria-label="After: smile with smoother skin"><b>AFTER</b></div>
<div class="abs shot" style="left:527px;top:2498px;width:282px;height:305px" role="img" aria-label="Before: close-up profile with crow's feet"><b>BEFORE</b></div>
<div class="abs shot" style="left:841px;top:2498px;width:286px;height:305px" role="img" aria-label="After: close-up profile with smoother skin"><b>AFTER</b></div>
<div class="abs pill btn" style="left:509px;top:2841px;width:183px">Find Out More ›</div>

<!-- feedback -->
<svg class="band" style="top:2905px" width="370" height="400" viewBox="0 0 370 400" aria-hidden="true">
  <path d="M0 0L342 35V180L364 200L342 220V376H0Z" fill="var(--green)"/>
</svg>
<div class="abs panel" style="left:75px;top:3090px">
  <h2 style="font-size:36px">Feedback<br>Questions</h2>
</div>
<p class="abs fb-q">How likely are you to recommend Bright Path Family Medicine to a friend or colleague?</p>
<span class="abs scale-end" style="left:427px">Not Likely</span>
<span class="abs scale-end" style="left:990px">Extremely Likely</span>
<div class="abs scale">
  <span>0</span><span>1</span><span>2</span><span>3</span><span>4</span><span>5</span>
  <span class="hi">6</span><span class="hi">7</span><span class="hi">8</span><span class="hi">9</span><span class="hi">10</span>
</div>
<p class="abs fb-note">We value your feedback and strive to provide you with the best possible experience. If you have any suggestions on ways we can improve our care, please let us know. If we don't know there is a problem we can't fix it.</p>

<!-- footer -->
<svg class="band" style="top:3270px" width="1200" height="246" viewBox="0 0 1200 246" aria-hidden="true">
  <path d="M0 10C400 -10 800 -5 1200 20V246H0Z" fill="var(--footer)"/>
</svg>
<div class="abs foot-brand">
  <span class="brand-dot"></span>
  <span class="brand-name">Bright Path</span>
</div>
<p class="abs copyright">Copyright © 2017 Bright Path Family Medicine. All rights reserved.</p>
<div class="abs social" aria-label="Social links">
  <span></span><span></span><span></span><span></span>
</div>

</body>
</html>
```